6 page (for now) squarespace website design for a Mobile Fitness small business

My sons California based small business "BrellaFit Coaching" with new subsidiary called "BrellaFit 4 Kids". I don't understand coding the website, is that the function squarespace provides?
In the end I want a working website, squarespace, I have a google workspace domain, email and subscription to squarespace & google workspace. URLs include brellafitcoaching.example and brellafit4kids.example. I have an idea of what I am looking for in a website and I have some examples of website designs I like, but I am 100% open to your design concepts and artistic flair. email is morgan@brellafitcoaching.example
I am looking for someone to design the site, help me understand how to make "minor" changes and hopefully have a long term relationship on the tech side of the business. I need an Idea of pricing for future changes (Rate T&M).
There are 2 businesses so I need a way to incorporate both the main company and a subsidiary into 1 website or link it somehow. I am open to your suggestions how to accomplish that. Do I need 2 completely separate websites or can it be done on 1 site directing you to different pages. I read conflicting info if it is a BAD idea to link 2 different websites so I will defer to your advice.
Below are the pages I need designed:
- Home Page- BrellaFit Coaching
- Home Page- BrellaFit 4 Kids (Homeschool market)
- Member Page (subscription service?)
- Workouts- with video clips 1-6 min each
- About
- Contact
- FAQ's
Future work & page designs:
- Store with training subscriptions & a few merch items
- Booking Appointments
- Bookshelf
- email campaign
-Blog
I like the feel of this website:
https://quillstride.example/

```html
<!DOCTYPE html>
<html lang="en">
<head>
<meta charset="utf-8">
<title>BrellaFit Coaching — Contact</title>
<link rel="stylesheet" href="https://fonts.googleapis.com/css2?family=Rajdhani:wght@300;700&family=Montserrat:ital,wght@0,400;0,500;0,700;1,400;1,700&display=swap">
<style>
  :root {
    --nav-bg: #1f2023;
    --ink-dark: #0d0d0e;
    --panel-dark: #18181a;
    --footer-bg: #19191b;
    --white: #ffffff;
    --muted: #8d8f94;
    --heading-grey: #4a4b4f;
    --body-grey: #5d5f64;
    --field-bg: #eeeeef;
    --placeholder: #9a9ca1;
    --accent: #ec9a12;
    --teal: #2bb39a;
    --btn-start: #f05a28;
    --btn-end: #f7a43a;
    --cta-orange: #f39a1e;
  }
  * { box-sizing: border-box; margin: 0; padding: 0; }
  html, body { width: 1200px; height: 2478px; overflow: hidden; }
  body { position: relative; background: var(--white); font-family: "Montserrat", sans-serif; color: var(--white); }
  .abs { position: absolute; }

  /* Top navigation */
  .site-nav { left: 0; top: 0; width: 1200px; height: 62px; background: var(--nav-bg); }
  .brand { display: flex; align-items: center; gap: 16px; }
  .brand-mark { width: 30px; height: 30px; border: 2px solid var(--white); border-radius: 50%; }
  .brand-name { font-family: "Montserrat", sans-serif; font-weight: 400; font-size: 22px; letter-spacing: 6px; color: var(--white); }
  .site-nav .brand { position: absolute; left: 52px; top: 16px; }
  .nav-links { position: absolute; left: 382px; top: 25px; display: flex; gap: 30px; list-style: none; }
  .nav-links li { font-size: 10px; letter-spacing: 2px; color: var(--muted); text-transform: uppercase; }
  .nav-links li.is-current { color: var(--white); font-weight: 700; border-bottom: 2px solid var(--accent); padding-bottom: 4px; }
  .nav-social { position: absolute; right: 27px; top: 26px; display: flex; gap: 12px; align-items: center; }
  .dot-icon { width: 10px; height: 10px; border-radius: 50%; border: 1.5px solid var(--muted); }

  /* Hero */
  .hero { left: 0; top: 62px; width: 1200px; height: 453px;
    background: radial-gradient(ellipse 380px 300px at 330px 300px, #3a2a22 0%, #1a1614 55%, var(--ink-dark) 100%); }
  .hero-title { position: absolute; right: 99px; top: 100px; text-align: right; font-family: "Rajdhani", sans-serif; text-transform: uppercase; line-height: 76px; font-size: 74px; }
  .hero-title .line-strong { font-weight: 700; display: block; }
  .hero-title .line-accent { font-weight: 700; color: var(--accent); display: block; }
  .hero-title .line-light { font-weight: 300; display: block; }

  /* Map + contact strip */
  .map-area { left: 0; top: 515px; width: 599px; height: 456px; background: linear-gradient(160deg, #3a3a3c, #2c2c2e); }
  .map-zoom { position: absolute; left: 10px; top: 10px; width: 36px; height: 73px; background: var(--white); border-radius: 2px; color: #555; font-size: 24px; text-align: center; line-height: 36px; }
  .contact-panel { left: 599px; top: 515px; width: 601px; height: 456px;
    background: radial-gradient(ellipse 220px 300px at 500px 200px, #4a3a30 0%, #221d1a 60%, var(--panel-dark) 100%); }
  .info-label { font-size: 13px; font-weight: 700; font-style: italic; letter-spacing: 1px; color: var(--white); text-transform: uppercase; }
  .info-label::after { content: ""; display: block; width: 26px; height: 2px; background: var(--teal); margin-top: 10px; }
  .info-value { font-size: 16px; color: var(--white); letter-spacing: .5px; white-space: nowrap; }
  .social-row { display: flex; gap: 26px; align-items: center; }
  .social-row .dot-icon { width: 18px; height: 18px; border: 2px solid #c9cacd; }

  /* Email form section */
  .email-section { left: 0; top: 971px; width: 1200px; height: 786px; background: var(--white); }
  .section-title { position: absolute; left: 100px; top: 110px; font-family: "Rajdhani", sans-serif; font-weight: 700; font-size: 32px; letter-spacing: .5px; color: var(--heading-grey); }
  .section-title::after { content: ""; display: block; width: 62px; height: 2px; background: var(--heading-grey); margin-top: 6px; }
  .section-intro { position: absolute; left: 100px; top: 178px; width: 480px; font-size: 15px; line-height: 23px; color: var(--body-grey); letter-spacing: .3px; }
  .field { position: absolute; left: 100px; width: 300px; height: 37px; background: var(--field-bg); font-size: 12px; font-style: italic; color: var(--placeholder); padding: 12px 13px; }
  .field-message { width: 396px; height: 145px; }
  .btn { position: absolute; height: 40px; width: 158px; background: linear-gradient(90deg, var(--btn-start), var(--btn-end)); color: var(--white); font-size: 13px; font-weight: 700; letter-spacing: .5px; text-align: center; line-height: 40px; text-transform: uppercase; }
  .portrait { position: absolute; left: 655px; top: 116px; width: 390px; height: 481px; background: linear-gradient(135deg, #8a5a3a 0%, #c79272 40%, #6b4634 75%, #2f2521 100%); }
  .pattern-fade { position: absolute; left: 1045px; top: 180px; width: 90px; height: 350px; border-radius: 0 175px 175px 0; background: radial-gradient(ellipse at left center, #e6e7ea 0%, #f6f6f7 70%, var(--white) 100%); }

  /* Call to action */
  .cta-band { left: 0; top: 1757px; width: 1200px; height: 438px;
    background: radial-gradient(ellipse 420px 330px at 600px 200px, #3c2c24 0%, #1f1915 55%, #0f0d0c 100%); }
  .cta-title { position: absolute; left: 0; top: 92px; width: 1200px; text-align: center; font-family: "Rajdhani", sans-serif; font-weight: 700; font-size: 66px; line-height: 62px; text-transform: uppercase; letter-spacing: 1px; }
  .cta-title .accent { color: var(--cta-orange); }

  /* Footer */
  .site-footer { left: 0; top: 2195px; width: 1200px; height: 283px; background: var(--footer-bg); }
  .footer-col { position: absolute; top: 46px; }
  .footer-col .info-label { font-size: 11px; }
  .footer-col .info-label::after { width: 20px; margin-top: 6px; }
  .footer-col .info-value { font-size: 12px; margin-top: 22px; letter-spacing: .3px; }
  .footer-col .social-row { gap: 18px; margin-top: 20px; }
  .footer-col .social-row .dot-icon { width: 14px; height: 14px; }
  .footer-brand { position: absolute; left: 0; top: 150px; width: 1200px; display: flex; flex-direction: column; align-items: center; gap: 12px; }
  .footer-brand .brand-mark { width: 44px; height: 44px; }
  .footer-brand .brand-name { font-size: 20px; }
  .footer-links { position: absolute; left: 0; top: 2439px; width: 1200px; display: flex; justify-content: center; gap: 30px; list-style: none; }
  .footer-links li { font-size: 10px; letter-spacing: 2px; color: var(--muted); text-transform: uppercase; }
</style>
</head>
<body>

<header class="abs site-nav">
  <div class="brand"><span class="brand-mark"></span><span class="brand-name">BRELLAFIT</span></div>
  <ul class="nav-links">
    <li>Home</li><li>About</li><li>Workouts</li><li>Membership</li><li>Shop</li><li class="is-current">Contact</li>
  </ul>
  <div class="nav-social">
    <span class="dot-icon" aria-label="Social profile"></span>
    <span class="dot-icon" aria-label="Social profile"></span>
    <span class="dot-icon" aria-label="Social profile"></span>
    <svg width="12" height="9" viewBox="0 0 12 9" aria-label="Email"><rect x="0" y="0" width="12" height="9" rx="1" fill="#8d8f94"/><path d="M0 1 L6 5 L12 1" stroke="#1f2023" stroke-width="1.2" fill="none"/></svg>
  </div>
</header>

<section class="abs hero" role="img" aria-label="Athlete in a dark hooded jacket, lit from above">
  <h1 class="hero-title">
    <span class="line-strong">Let’s</span>
    <span class="line-accent">Accomplish</span>
    <span class="line-light">Today!</span>
  </h1>
</section>

<div class="abs map-area" role="img" aria-label="Dark-styled street map marking the gym location">
  <div class="map-zoom">+<br>−</div>
</div>

<section class="abs contact-panel" role="img" aria-label="Athlete in sports top, dimly lit">
  <div class="abs" style="left:56px;top:70px;">
    <p class="info-label">Mobile</p>
    <p class="info-value" style="margin-top:14px;">(555) 014-2290</p>
  </div>
  <div class="abs" style="left:56px;top:182px;">
    <p class="info-label">Email</p>
    <p class="info-value" style="margin-top:14px;">morgan@brellafitcoaching.example</p>
  </div>
  <div class="abs" style="left:56px;top:294px;">
    <p class="info-label">Social</p>
    <div class="social-row" style="margin-top:24px;">
      <span class="dot-icon" aria-label="Social profile"></span>
      <span class="dot-icon" aria-label="Social profile"></span>
      <span class="dot-icon" aria-label="Social profile"></span>
      <svg width="24" height="18" viewBox="0 0 24 18" aria-label="Email"><rect width="24" height="18" rx="2" fill="#c9cacd"/><path d="M1 2 L12 10 L23 2" stroke="#221d1a" stroke-width="2" fill="none"/></svg>
    </div>
  </div>
</section>

<section class="abs email-section">
  <h2 class="section-title">EMAIL US</h2>
  <p class="section-intro">Lorem ipsum dolor sit amet, consectetuer adipiscing elit, sed diam nonummy nibh euismod tincidunt ut laoreet dolore</p>
  <div class="field" style="top:279px;">Your Name</div>
  <div class="field" style="top:341px;">E-Mail</div>
  <div class="field" style="top:404px;">Subject</div>
  <div class="field field-message" style="top:471px;">Your Message</div>
  <div class="btn" style="left:101px;top:664px;">Send Message</div>
  <div class="pattern-fade" role="img" aria-label="Soft dotted half-circle decoration"></div>
  <div class="portrait" role="img" aria-label="Portrait of a coach resting his chin on clasped hands"></div>
</section>

<section class="abs cta-band" role="img" aria-label="Athlete seated with arms raised behind the head">
  <h2 class="cta-title">Lorem<br>Ipsum<br><span class="accent">Dolor<br>Sit Amet</span></h2>
  <div class="btn" style="left:521px;top:356px;">Book Session</div>
</section>

<footer class="abs site-footer">
  <div class="footer-col" style="left:250px;">
    <p class="info-label">Mobile</p>
    <p class="info-value">(555) 014-2290</p>
  </div>
  <div class="footer-col" style="left:495px;">
    <p class="info-label">Email</p>
    <p class="info-value">morgan@brellafitcoaching.example</p>
  </div>
  <div class="footer-col" style="left:800px;">
    <p class="info-label">Social</p>
    <div class="social-row">
      <span class="dot-icon" aria-label="Social profile"></span>
      <span class="dot-icon" aria-label="Social profile"></span>
      <span class="dot-icon" aria-label="Social profile"></span>
      <svg width="17" height="12" viewBox="0 0 17 12" aria-label="Email"><rect width="17" height="12" rx="1.5" fill="#c9cacd"/><path d="M1 1.5 L8.5 7 L16 1.5" stroke="#19191b" stroke-width="1.5" fill="none"/></svg>
    </div>
  </div>
  <div class="footer-brand"><span class="brand-mark"></span><span class="brand-name">BRELLAFIT</span></div>
</footer>
<ul class="footer-links">
  <li>Home</li><li>About</li><li>Workouts</li><li>Membership</li><li>Shop</li><li>Contact</li>
</ul>

</body>
</html>
```